Web page for Gareth Pemblewick Chartered Tax Adviser

I need to take the basic web page that I have created and "Brand it" to be compatible with the corporate logo and stationery created for me by other Studio Flock designers.
I will need a watermark as well as a distinctive home page and then a branded general page for content including a series of Blogs.

Target Market(s)

My practice deals with expatriates including those looking to invest in Australia.

Industry/Entity Type

Crowd

Font styles to use
Other font styles liked:
• Per logo

Requirements
Must have
• Besides the homepage I will need a general page for content, branded in the same style as the letterheads.
Nice to have
• A watermark to go with the blogs and news content.

```html
<!DOCTYPE html>
<html lang="en">
<head>
<meta charset="utf-8">
<title>Gareth Pemblewick – Chartered Tax Adviser</title>
<link href="https://fonts.googleapis.com/css2?family=PT+Serif&family=Roboto:wght@400;500;700&display=swap" rel="stylesheet">
<style>
:root{
  --navy:#1f4a6e;
  --navy-dark:#163a58;
  --ink:#333;
  --muted:#666;
  --rule:#e3e3e3;
  --footer:#2b2b2b;
  --caption:rgba(60,60,60,.85);
}
*{box-sizing:border-box;margin:0;padding:0}
html,body{width:850px;height:1200px;overflow:hidden;background:#fff}
body{position:relative;font-family:"Roboto",sans-serif;color:var(--ink);border-top:2px solid var(--navy)}
.abs{position:absolute}
.brand{left:70px;top:30px;display:flex;align-items:center;gap:6px}
.brand-square{width:26px;height:26px;background:var(--navy)}
.brand-name{font-family:"PT Serif",serif;color:var(--navy);font-size:15px;line-height:1.15}
.brand-name small{display:block;font-size:7.5px;letter-spacing:2.6px;text-transform:uppercase}
.search{left:585px;top:34px;width:194px;height:26px;border:1px solid #ddd;font-size:8px;color:#999;padding:7px 9px}
.search svg{position:absolute;right:8px;top:7px}
.nav{left:70px;top:91px;width:710px;height:41px;background:linear-gradient(#2b5a80,var(--navy-dark));display:flex;list-style:none}
.nav li{font-family:"PT Serif",serif;color:#fff;font-size:10px;text-transform:uppercase;display:flex;align-items:center;justify-content:center;border-right:1px solid #47708f}
.nav li:last-child{border:0}
.hero{left:70px;top:136px;width:710px;height:344px;background:linear-gradient(135deg,#c9d6e0,#eef3f7 45%,#a7bccc);box-shadow:0 10px 12px -8px rgba(0,0,0,.45)}
.hero-caption{left:402px;top:141px;width:282px;height:128px;background:var(--caption);color:#fff;padding:14px 16px}
.hero-caption h2{font-weight:400;font-size:20px;margin-bottom:8px}
.hero-caption p{font-size:7.5px;line-height:16px;color:#eee}
.hero-arrows{right:24px;bottom:22px;display:flex;gap:2px}
.hero-arrows span{width:16px;height:16px;background:#777;color:#fff;font-size:10px;text-align:center;line-height:15px}
.welcome{left:70px;top:519px;width:710px;text-align:center}
.welcome h1{color:var(--navy);font-size:16px;font-weight:700;margin-bottom:10px}
.welcome p{font-size:7.3px;line-height:16px;color:var(--muted);padding:0 40px}
.divider{left:70px;top:618px;width:710px;height:1px;background:var(--rule)}
.sec-title{color:var(--navy);font-size:15px;font-weight:700}
.pager{left:543px;top:640px;font-size:10px;color:#aaa;letter-spacing:6px}
.post{left:70px;width:495px;height:200px}
.date{left:1px;top:0;width:47px;height:52px}
.date .day{height:24px;background:var(--navy);color:#fff;border-radius:24px 24px 0 0;text-align:center;font-weight:700;font-size:14px;line-height:26px;border:2px solid #fff;box-shadow:0 0 0 1px #ccc}
.date .mon{height:24px;background:#333;color:#fff;border-radius:0 0 24px 24px;text-align:center;font-size:12px;line-height:20px}
.post h3{left:62px;top:4px;width:332px;font-size:16px;font-weight:400;color:var(--navy);border-bottom:1px dashed #ccc;padding-bottom:3px}
.meta{left:62px;top:32px;font-size:7.5px;color:#666;display:flex;gap:20px}
.meta a{color:var(--navy)}
.thumb{left:1px;top:68px;width:182px;height:117px;border:3px solid #fff;box-shadow:0 1px 3px rgba(0,0,0,.35)}
.excerpt{left:200px;top:78px;width:295px;font-size:7.3px;line-height:16px;color:var(--muted);text-align:justify}
.more{left:200px;top:161px;width:62px;height:20px;border-radius:10px;background:var(--navy-dark);color:#fff;font-size:8px;font-weight:700;text-align:center;line-height:20px}
.news{left:586px;width:194px;height:75px;border-bottom:1px solid #ddd}
.news .pic{width:40px;height:40px;border:2px solid #fff;box-shadow:0 1px 3px rgba(0,0,0,.3)}
.news .txt{left:55px;top:0;width:140px;font-size:7px;line-height:13.5px;color:var(--muted)}
.news .txt b{color:var(--navy);font-weight:500}
.quote{left:586px;top:932px;width:194px;font-size:7.3px;line-height:15.6px;color:var(--muted);padding-left:17px}
.quote .mark{position:absolute;font-family:"PT Serif",serif;font-size:18px;color:#777}
.sig{left:601px;top:1054px;color:var(--navy);font-size:11px;font-weight:500}
.sig small{display:block;font-size:6.5px;color:#888;font-style:italic;font-weight:400}
footer{position:absolute;left:0;top:1110px;width:850px;height:90px;background:var(--footer);color:#fff}
.foot-nav{left:70px;top:25px;display:flex;gap:14px;font-size:7.5px;list-style:none}
.foot-nav li+li:before{content:"/";margin-right:14px}
.copy{left:70px;top:53px;font-size:7px}
.social{left:649px;top:32px;display:flex;gap:8px}
.social span{width:26px;height:24px;border:1.5px solid #ddd;border-radius:5px}
</style>
</head>
<body>
<div class="abs brand"><span class="brand-square"></span><span class="brand-name">Gareth Pemblewick<small>Chartered Tax Adviser</small></span></div>
<div class="abs search">Search :<svg width="9" height="9" viewBox="0 0 10 10"><circle cx="4" cy="4" r="3" fill="none" stroke="#999" stroke-width="1.3"/><path d="M6.3 6.3 9 9" stroke="#999" stroke-width="1.3"/></svg></div>
<ul class="abs nav">
  <li style="width:86px">Home</li><li style="width:98px">About us</li><li style="width:99px">Services</li><li style="width:81px">News</li><li style="width:112px">Latest blog</li><li style="width:117px">Testimonials</li><li style="width:117px">Contact us</li>
</ul>
<div class="abs hero" role="img" aria-label="Photo of colleagues reviewing printed charts on a glass table">
  <div class="abs hero-caption"><h2>GARETH PEMBLEWICK</h2><p>It is a long established fact that a reader will be distracted by the readable content of a page when looking at its layout. The point of using Lorem Ipsum is that it has a more-or-less normal distribution of letters, here, content here', making it look like readable English.......</p></div>
  <div class="abs hero-arrows"><span>‹</span><span>›</span></div>
</div>
<section class="abs welcome"><h1>WELCOME TO GARETH PEMBLEWICK</h1><p>It is a long established fact that a reader will be distracted by the readable content of a page when looking at its layout. The point of using Lorem Ipsum is that it has a more-or-less normal distribution of letters, as opposed to using 'Content here, content here', making it look like readable English. Many desktop publishing packages and web page editors default model text, and a search for 'lorem ipsum' will uncover many web sites still in their infancy.</p></section>
<div class="abs divider"></div>
<h2 class="abs sec-title" style="left:70px;top:636px">LATEST BLOG</h2>
<div class="abs pager">‹ ›</div>
<article class="abs post" style="top:676px">
  <div class="abs date"><div class="day">19</div><div class="mon">Dec</div></div>
  <h3 class="abs">Neque porro quisquam dolorem ipsum</h3>
  <div class="abs meta"><span>Published in <a>Photography</a></span><span>Written by <a>Admin</a></span><span>Comments <a>277</a></span></div>
  <div class="abs thumb" style="background:linear-gradient(135deg,#d8e2ea,#f4f7f9 60%,#b9c7d2)" role="img" aria-label="Photo of two businessmen shaking hands in a bright office"></div>
  <p class="abs excerpt">Nam libero tempore, cum soluta nobis est eligendi optio cumque nihil impedit quo minus id quod maxime placeat facere possimus, omnis voluptas assumenda est, omnis dolor repellendus. Temporibus autem quibusdam et aut officiis debitis aut rerum necessitatibus saepe ribus autem quibusdam et aut officiis debitis aut rerum It ipage when looking at its layout.</p>
  <div class="abs more">Read More</div>
</article>
<article class="abs post" style="top:886px">
  <div class="abs date"><div class="day">19</div><div class="mon">Dec</div></div>
  <h3 class="abs">Neque porro quisquam dolorem ipsum</h3>
  <div class="abs meta"><span>Published in <a>Photography</a></span><span>Written by <a>Admin</a></span><span>Comments <a>277</a></span></div>
  <div class="abs thumb" style="background:linear-gradient(135deg,#c9b8a6,#e9e4de 50%,#3a3f4a)" role="img" aria-label="Photo of a business team meeting around a table"></div>
  <p class="abs excerpt">Nam libero tempore, cum soluta nobis est eligendi optio cumque nihil impedit quo minus id quod maxime placeat facere possimus, omnis voluptas assumenda est, omnis dolor repellendus. Temporibus autem quibusdam et aut officiis debitis aut rerum necessitatibus saepe ribus autem quibusdam et aut officiis debitis aut rerum It ipage when looking at its layout.</p>
  <div class="abs more">Read More</div>
</article>
<h2 class="abs sec-title" style="left:585px;top:636px">LATEST NEWS</h2>
<div class="abs news" style="top:677px"><div class="pic" style="background:linear-gradient(#dfe7ee,#9fb0bd)" role="img" aria-label="Photo of a business meeting"></div><p class="abs txt"><b>Tuesday 25,2014</b><br>It is a long established fact that a reader will be distracted by the readable content of a page when looking at its layout.</p></div>
<div class="abs news" style="top:752px"><div class="pic" style="background:linear-gradient(#e3e3e3,#34383f)" role="img" aria-label="Photo of a businessman at a desk"></div><p class="abs txt"><b>Tuesday 25,2014</b><br>It is a long established fact that a reader will be distracted by the readable content of a page when looking at its layout.</p></div>
<div class="abs news" style="top:826px"><div class="pic" style="background:linear-gradient(#d9c2ad,#4a3a34)" role="img" aria-label="Photo of colleagues reviewing documents"></div><p class="abs txt"><b>Tuesday 25,2014</b><br>It is a long established fact that a reader will be distracted by the readable content of a page when looking at its layout.</p></div>
<h2 class="abs sec-title" style="left:587px;top:904px">TESTIMONIALS</h2>
<blockquote class="abs quote"><span class="mark" style="left:0;top:-6px">“</span>It is a long established fact that a reader will be distracted by the readable content of a page when looking at its layout. The point of using Lorem Ipsum is that it has a more-or-less normal distribu-tion of letters, as opposed to using 'Content here, content here', making it look like readable English. web sites still in their infancy.<span class="mark" style="right:50px;bottom:-14px">”</span></blockquote>
<div class="abs sig">Alan Brooke<small>posts on Aug 25 2014</small></div>
<footer>
  <ul class="abs foot-nav"><li>HOME</li><li>ABOUT US</li><li>SERVICES</li><li>NEWS</li><li>LATEST BLOG</li><li>TESTIMONIALS</li><li>CONTACT US</li></ul>
  <p class="abs copy">© Copy right 2014 Gareth Pemblewick. All Rights Reserved</p>
  <div class="abs social" aria-label="Social links"><span></span><span></span><span></span><span></span></div>
</footer>
</body>
</html>
```